Fitness Coach Needs Book Cover Created

I would like a book cover created for my upcoming project titled,
Golden Stride After 40: 7 Quiet Rules to Reshape Every Day

Target Market(s)

Men & Women 30-40 years old

Industry/Entity Type

Fitness

Font styles to use
Serif

Requirements
Must have
• 3 color cover. I have attached my name to be used at bottom of cover and uploaded a couple sample covers as well.
Should not have
• stock imaging.

```html
<!DOCTYPE html>
<html lang="en">
<head>
<meta charset="UTF-8">
<title>Golden Stride After 40 — Book Cover</title>
<link rel="stylesheet" href="https://fonts.googleapis.com/css2?family=Cormorant+Garamond:wght@400;500&family=Playfair+Display:wght@700;800;900&display=swap">
<style>
  :root {
    --sky-light: #74c6e8;
    --sky-mid: #3f9fd2;
    --sky-deep: #1c6aa3;
    --navy: #061a2d;
    --ink: #0b1f33;
    --white: #ffffff;
  }
  html, body {
    margin: 0;
    padding: 0;
    width: 800px;
    height: 1200px;
    overflow: hidden;
  }
  .cover {
    position: relative;
    width: 800px;
    height: 1200px;
    overflow: hidden;
    background:
      radial-gradient(ellipse 75% 60% at 50% 52%, var(--sky-light) 0%, var(--sky-mid) 55%, var(--sky-deep) 100%);
  }
  .cover::after {
    content: "";
    position: absolute;
    inset: 0;
    background:
      linear-gradient(to bottom, rgba(10,60,110,0.45) 0%, rgba(10,60,110,0) 18%, rgba(10,60,110,0) 80%, rgba(10,60,110,0.45) 100%);
    pointer-events: none;
  }
  .kicker {
    position: absolute;
    top: 212px;
    left: 0;
    width: 100%;
    margin: 0;
    text-align: center;
    color: var(--white);
    font-family: "Cormorant Garamond", Georgia, serif;
    font-weight: 500;
    font-size: 50px;
    letter-spacing: 0.04em;
    line-height: 1;
    z-index: 1;
  }
  .headline {
    position: absolute;
    top: 272px;
    left: 0;
    width: 100%;
    margin: 0;
    text-align: center;
    color: var(--ink);
    font-family: "Playfair Display", Georgia, serif;
    font-weight: 900;
    font-size: 120px;
    font-variant-numeric: lining-nums;
    letter-spacing: 0;
    line-height: 1;
    white-space: nowrap;
    z-index: 1;
  }
  .subtitle-band {
    position: absolute;
    top: 460px;
    left: 0;
    width: 100%;
    height: 170px;
    background: var(--navy);
    display: flex;
    align-items: center;
    justify-content: center;
    z-index: 1;
  }
  .subtitle {
    margin: 0;
    text-align: center;
    color: var(--white);
    font-family: "Cormorant Garamond", Georgia, serif;
    font-weight: 500;
    font-size: 38px;
    font-variant-numeric: lining-nums;
    letter-spacing: 0.1em;
    line-height: 1.25;
  }
  .author {
    position: absolute;
    top: 1110px;
    left: 0;
    width: 100%;
    margin: 0;
    text-align: center;
    color: var(--ink);
    font-family: "Playfair Display", Georgia, serif;
    font-weight: 800;
    font-size: 46px;
    letter-spacing: 0.04em;
    line-height: 1;
    z-index: 1;
  }
</style>
</head>
<body>
  <main class="cover">
    <p class="kicker">GOLDEN STRIDE</p>
    <h1 class="headline">AFTER 40:</h1>
    <div class="subtitle-band">
      <p class="subtitle">7 QUIET RULES TO<br>RESHAPE EVERY DAY</p>
    </div>
    <p class="author">MARA ELLISON</p>
  </main>
</body>
</html>
```